Web design project for exciting Australian start-up

Background
We are looking for a creative and talented web design artist to work alongside our market leading web developer.
• You will be required to create a modern and clean design theme for our website, incorporating selected rustic colour scheme elements for our exciting Australian start-up to operate within the coffee industry.
reoccurring work to be expected to flow to the successful designer.
Requirements
• c. 5 - 10 page website
• Landing page
• Log in/ out
• 404 template
• Typography is emphasised
• Please use either a) typevane.com, b) free web fonts, c) marlo fonts
• All design elements in vector format
• Preferably with icons for each header title(i.e. about us, how it works etc) but designer have free reign over how the site looks, so might not be applicable
• All pages to be responsive
• Down to iPad resolution

High level visual design brief attached - additional pages to be worked from base design.

Design inspiration
• We would like to use design elements from the following sources:
http://www.brivantel.com/sorvik/ (Functionality)
Colour scheme refer to logo and complementary style guide
Updates

```html
<!DOCTYPE html>
<html lang="en">
<head>
<meta charset="utf-8">
<title>Brewline – Dashboard</title>
<link rel="stylesheet" href="https://fonts.googleapis.com/css2?family=Cabin:wght@400;500;600;700&family=Roboto+Slab:wght@400;500&family=Oswald:wght@500&display=swap">
<style>
:root{
  --red:#c43c3f;
  --red-btn:#e8393e;
  --red-soft:#d24f52;
  --orange:#fda032;
  --brown:#7b4c40;
  --brown-light:#c79a7c;
  --ink:#1b1b1b;
  --slate:#4a4a4a;
  --line:#e2e2e2;
  --muted:#8a8a8a;
  --footer:#e8e8e8;
  --footer-dark:#474747;
  --white:#ffffff;
}
*{box-sizing:border-box;margin:0;padding:0}
html,body{width:1200px;height:1195px;overflow:hidden;background:var(--white);font-family:"Cabin",sans-serif;color:var(--ink)}
.page{position:relative;width:1200px;height:1195px}
.abs{position:absolute}

/* header */
.site-header{position:absolute;left:0;top:0;width:1200px;height:107px;border-bottom:1px solid #e6e6e6;box-shadow:0 1px 3px rgba(0,0,0,.05)}
.brand{position:absolute;left:161px;top:36px;display:flex;align-items:center;gap:10px;font-family:"Oswald",sans-serif;font-size:26px;letter-spacing:2px;color:var(--ink)}
.brand-dot{width:26px;height:26px;border-radius:50%;background:var(--orange)}
.main-nav{position:absolute;left:423px;top:0;display:flex;height:107px}
.nav-item{height:107px;border-left:1px solid #ececec;display:flex;flex-direction:column;align-items:center;justify-content:center;gap:8px;font-size:12px;color:#444;text-transform:uppercase}
.nav-item:last-child{border-right:1px solid #ececec}
.nav-item svg{width:20px;height:20px}
.header-actions{position:absolute;top:38px;left:758px;display:flex;gap:9px}
.btn{height:31px;display:flex;align-items:center;justify-content:center;color:#fff;font-size:14px;border-radius:2px}
.btn-red{background:var(--red-btn)}
.btn-orange{background:var(--orange)}

/* panels */
.panel-title{font-weight:700;font-size:18px;color:#fff;text-transform:uppercase}
.photos{left:161px;top:129px;width:232px;height:319px;background:var(--brown)}
.photos .panel-title{position:absolute;left:17px;top:22px}
.arrows{position:absolute;right:17px;top:19px;display:flex;gap:4px}
.round-arrow{width:24px;height:24px;border-radius:50%;background:var(--brown-light);display:flex;align-items:center;justify-content:center}
.photo-frame{position:absolute;left:17px;top:54px;width:199px;height:155px;border:4px solid var(--brown-light);background:radial-gradient(circle at 45% 40%,#f4f1ea 0 22%,#b9b8b4 32%,#6f4632 55%,#3c2418 100%)}
.cafe-info{position:absolute;left:0;top:224px;width:232px;text-align:center;color:#fff;font-size:13px;line-height:20.5px}

.account{left:161px;top:465px;width:232px;height:264px;background:var(--red)}
.account .panel-title{position:absolute;left:17px;top:20px}
.acc-row{position:absolute;left:0;width:232px;display:flex;align-items:center;justify-content:space-between;padding:0 22px 0 17px;color:#fff;font-size:15px}
.acc-row.soft{background:var(--red-soft)}
.acc-sub{display:block;font-size:12px;line-height:14px;margin-top:3px;opacity:.95}
.tick{width:34px;height:34px;border-radius:50%;background:#3a2a26;display:flex;align-items:center;justify-content:center}

/* middle */
.section-title{font-weight:600;font-size:18px;text-transform:uppercase;color:var(--ink)}
.digit{position:absolute;top:183px;width:56px;height:56px;display:flex;align-items:center;justify-content:center;font-weight:700;font-size:34px;color:#fff}
.digit.o{background:var(--orange)} .digit.k{background:var(--ink)}
.rule{left:424px;top:267px;width:374px;height:1px;background:var(--line)}
.purchases{left:424px;top:320px;width:374px;border:1px solid #dcdcdc;border-collapse:collapse;font-size:12px;color:var(--muted)}
.purchases th{height:46px;background:#ececec;font-weight:400;color:#444;font-size:13px;text-align:left;padding-left:14px;border-right:1px solid #dcdcdc}
.purchases th span{display:inline-block;margin-left:6px;border:4px solid transparent;border-top:5px solid #999;transform:translateY(3px)}
.purchases td{height:45.4px;border-top:1px solid #e2e2e2;border-right:1px solid #e2e2e2}
.purchases td:first-child{padding-left:22px}
.purchases td:nth-child(2){text-align:center}
.purchases tr:nth-child(odd) td{background:#f0f0f0}
.purchases tr:nth-child(even) td{background:#f6f6f6}

/* right */
.inbox{left:829px;top:129px;width:210px;height:130px;background:var(--brown)}
.inbox .panel-title{position:absolute;left:25px;top:22px}
.inbox-row{position:absolute;left:0;width:210px;height:31px;display:flex;align-items:center;padding-left:25px;color:#fff;font-size:12.5px;gap:6px}
.inbox-row.active{background:var(--brown-light)}
.caret{border:4px solid transparent;border-top:5px solid #fff;transform:translateY(2px)}
.deliveries{left:829px;top:275px;width:210px;height:282px;background:var(--slate)}
.deliv-head{height:83px;background:var(--red);color:#fff;text-align:center;font-family:"Roboto Slab",serif;font-size:14px;line-height:21px;padding-top:22px;position:relative}
.mini-arrows{position:absolute;left:85px;top:75px;display:flex;gap:5px}
.mini-arrows div{width:18px;height:18px;background:var(--red-btn);display:flex;align-items:center;justify-content:center}
.deliv-item{margin:0 25px;padding:32px 4px 18px;color:#fff;font-size:12px;line-height:16px}
.deliv-item+.deliv-item{border-top:1px solid #6a6a6a;padding-top:14px}
.deliv-item b{font-weight:700;display:block;margin-bottom:2px}

.calendar{left:829px;top:570px;width:210px;border:1px solid #ddd;border-top:0}
.cal-head{height:32px;background:var(--orange);color:#fff;display:flex;align-items:center;justify-content:space-between;padding:0 10px;font-size:16px;margin:0 -1px}
.cal-grid{display:grid;grid-template-columns:repeat(7,1fr)}
.dow{height:24px;font-size:9px;color:#888;display:flex;align-items:center;justify-content:center;border-bottom:1px solid #ddd}
.day{height:30px;display:flex;align-items:center;justify-content:center;font-size:12px;color:#555;border-right:1px solid #e4e4e4;border-bottom:1px solid #e4e4e4}
.day:nth-child(7n){border-right:0}
.day.today{background:var(--orange);color:#fff;font-weight:700}
.day.mark{background:#ececec}
.day.dim{color:#bbb}
.download{left:829px;top:793px;width:210px;height:44px;background:var(--red);color:#fff;display:flex;align-items:center;gap:18px;padding-left:22px;font-size:17px;font-weight:600}

/* footer */
.site-footer{position:absolute;left:0;top:890px;width:1200px;height:235px;background:var(--footer)}
.foot-col{position:absolute;top:50px}
.foot-col h3{font-family:"Roboto Slab",serif;font-weight:400;font-size:17px;color:var(--ink);margin-bottom:18px}
.foot-col li{list-style:none;font-family:"Roboto Slab",serif;font-size:13.5px;color:#444;height:31px;display:flex;align-items:center;gap:14px}
.soc{width:10px;height:10px;background:#555;border-radius:2px}
.bottom-bar{position:absolute;left:0;top:1125px;width:1200px;height:70px;background:var(--footer-dark)}
.bottom-bar .inner{position:absolute;left:161px;top:6px;width:878px;border-top:1px solid #5c5c5c;text-align:center;color:#fff;font-family:"Roboto Slab",serif;font-size:13.5px;padding-top:16px}
</style>
</head>
<body>
<div class="page">

<header class="site-header">
  <div class="brand"><span>BREWLINE</span><span class="brand-dot"></span></div>
  <nav class="main-nav">
    <div class="nav-item" style="width:94px">
      <svg viewBox="0 0 20 20" fill="none" stroke="#fda032" stroke-width="1.3"><path d="M3 9l7-6 7 6M5 8v9h10V8M8 17v-5h4v5"/></svg>About us</div>
    <div class="nav-item" style="width:136px">
      <svg viewBox="0 0 20 20" fill="none" stroke="#888" stroke-width="1.2"><circle cx="8" cy="7" r="3"/><path d="M3 17c0-3 2-5 5-5s5 2 5 5"/><rect x="12" y="2" width="6" height="5"/></svg>How it works</div>
    <div class="nav-item" style="width:65px">
      <svg viewBox="0 0 20 20" fill="none" stroke="#888" stroke-width="1.2"><rect x="4" y="4" width="4" height="13"/><rect x="11" y="2" width="5" height="15"/></svg>FAQ</div>
  </nav>
  <div class="header-actions">
    <div class="btn btn-red" style="width:110px">Marketplace</div>
    <div class="btn btn-orange" style="width:76px">Login</div>
    <div class="btn btn-red" style="width:76px">Sign up</div>
  </div>
</header>

<section class="abs photos">
  <h2 class="panel-title">Photos</h2>
  <div class="arrows">
    <div class="round-arrow"><svg width="8" height="10" viewBox="0 0 8 10"><path d="M6 1L2 5l4 4" stroke="#fff" stroke-width="1.5" fill="none"/></svg></div>
    <div class="round-arrow"><svg width="8" height="10" viewBox="0 0 8 10"><path d="M2 1l4 4-4 4" stroke="#fff" stroke-width="1.5" fill="none"/></svg></div>
  </div>
  <div class="photo-frame" role="img" aria-label="Photo of a cup of coffee on a saucer with sugar cubes"></div>
  <div class="cafe-info">Café Loriel<br>Melbourne, Australia<br>Member since [Feb, 2014]</div>
</section>

<section class="abs account">
  <h2 class="panel-title">My Account</h2>
  <div class="acc-row soft" style="top:62px;height:46px"><span>Email Address</span>
    <div class="tick"><svg width="14" height="12" viewBox="0 0 14 12"><path d="M1 6l4 4 8-8" stroke="#fff" stroke-width="2.5" fill="none"/></svg></div></div>
  <div class="acc-row" style="top:108px;height:102px;align-items:flex-start;padding-top:21px"><span>Café type<span class="acc-sub">(i.e. Café, speciality coffee&nbsp; shop, restaurant)</span></span></div>
  <div class="acc-row soft" style="top:212px;height:52px"><span>Payment details</span>
    <div class="tick"><svg width="14" height="12" viewBox="0 0 14 12"><path d="M1 6l4 4 8-8" stroke="#fff" stroke-width="2.5" fill="none"/></svg></div></div>
</section>

<h2 class="abs section-title" style="left:425px;top:149px">Live Tenders</h2>
<div class="digit o" style="left:424px">0</div>
<div class="digit k" style="left:482px">1</div>
<div class="digit o" style="left:555px">0</div>
<div class="digit k" style="left:611px">8</div>
<div class="digit o" style="left:685px">1</div>
<div class="digit k" style="left:742px">4</div>
<div class="abs rule"></div>

<h2 class="abs section-title" style="left:425px;top:290px">Purchases</h2>
<table class="abs purchases">
  <thead><tr><th style="width:77px">All<span></span></th><th style="width:138px;padding-left:8px">Period (x months)<span></span></th><th style="padding-left:8px">Awaiting feedback (x)<span></span></th></tr></thead>
  <tbody>
    <tr><td>Pro-1</td><td>March</td><td></td></tr>
    <tr><td>Pro-2</td><td>March</td><td></td></tr>
    <tr><td>Pro-3</td><td>March</td><td></td></tr>
    <tr><td>Pro-4</td><td>March</td><td></td></tr>
    <tr><td>Pro-5</td><td>March</td><td></td></tr>
    <tr><td>Pro-6</td><td>March</td><td></td></tr>
    <tr><td>Pro-7</td><td>March</td><td></td></tr>
    <tr><td>Pro-8</td><td>March</td><td></td></tr>
  </tbody>
</table>

<section class="abs inbox">
  <h2 class="panel-title">Inbox</h2>
  <div class="inbox-row active" style="top:52px"><span class="caret"></span>Messages</div>
  <div class="inbox-row" style="top:89px"><span class="caret"></span>Saved searches</div>
</section>

<section class="abs deliveries">
  <div class="deliv-head">INCOMING DELIVERIES<br>THIS WEEK
    <div class="mini-arrows">
      <div><svg width="6" height="8"><path d="M5 0v8L0 4z" fill="#fff"/></svg></div>
      <div><svg width="6" height="8"><path d="M0 0v8l5-4z" fill="#fff"/></svg></div>
    </div>
  </div>
  <div class="deliv-item"><b>8 AM – 11 AM</b>Delivery of order 3220x<br>Order: 20kg Harbor Beans</div>
  <div class="deliv-item"><b>8 AM – 11 AM</b>Delivery of order 3220x<br>Order: 20kg Harbor Beans</div>
</section>

<section class="abs calendar">
  <div class="cal-head">
    <svg width="9" height="14" viewBox="0 0 9 14"><path d="M7 1L2 7l5 6" stroke="#fff" stroke-width="2" fill="none"/></svg>
    <span>MARCH 2014</span>
    <svg width="9" height="14" viewBox="0 0 9 14"><path d="M2 1l5 6-5 6" stroke="#fff" stroke-width="2" fill="none"/></svg>
  </div>
  <div class="cal-grid">
    <div class="dow">SUN</div><div class="dow">MON</div><div class="dow">TUE</div><div class="dow">WED</div><div class="dow">THU</div><div class="dow">FRI</div><div class="dow">SAT</div>
    <div class="day"></div><div class="day">1</div><div class="day">2</div><div class="day">3</div><div class="day">4</div><div class="day">5</div><div class="day">6</div>
    <div class="day">7</div><div class="day">8</div><div class="day">9</div><div class="day">10</div><div class="day">11</div><div class="day mark">12</div><div class="day">13</div>
    <div class="day">14</div><div class="day">15</div><div class="day today">16</div><div class="day">17</div><div class="day">18</div><div class="day">19</div><div class="day">20</div>
    <div class="day">21</div><div class="day">22</div><div class="day">23</div><div class="day">24</div><div class="day">25</div><div class="day">26</div><div class="day">27</div>
    <div class="day">28</div><div class="day">29</div><div class="day">30</div><div class="day dim">31</div><div class="day"></div><div class="day"></div><div class="day"></div>
  </div>
</section>

<div class="abs download">
  <svg width="24" height="18" viewBox="0 0 24 18"><path d="M6 16a5 5 0 0 1-1-9.9A7 7 0 0 1 18.5 5 5.5 5.5 0 0 1 18 16z" fill="#fff"/><path d="M12 7v6M9 10.5l3 3 3-3" stroke="#c43c3f" stroke-width="2" fill="none"/></svg>
  Download
</div>

<footer class="site-footer">
  <div class="foot-col" style="left:295px">
    <h3>HELPFUL INFO</h3>
    <ul><li>About Us</li><li>Media Enquiries</li><li>Terms &amp; Conditions</li><li>Privacy Policy</li></ul>
  </div>
  <div class="foot-col" style="left:541px">
    <h3>WHO WE ARE</h3>
    <ul style="margin-left:8px"><li>How it works</li><li>FAQ</li><li>Contact us</li></ul>
  </div>
  <div class="foot-col" style="left:798px">
    <h3>JOIN US ON</h3>
    <ul style="margin-left:2px">
      <li style="width:90px;justify-content:space-between">Friendfold<span class="soc"></span></li>
      <li style="width:90px;justify-content:space-between">Chirpline<span class="soc"></span></li>
      <li style="width:90px;justify-content:space-between">Workweave<span class="soc"></span></li>
      <li style="width:90px;justify-content:space-between">Clipstream<span class="soc"></span></li>
    </ul>
  </div>
</footer>
<div class="bottom-bar"><div class="inner">Copyright © 2014 Brewline</div></div>

</div>
</body>
</html>
```